New Business Card for Casual Beachfront Cafe

Quirky Beachfront Cafe at Gullhaven, South Australia needs a DOUBLE SIDED business card to print on PrintHollow.

Target Market(s)

Business Cards sit on the counter for Guests to take with them. Please view our website www.saltkettlecafe.com.au to get a feel for the Cafe. You may also view our Instagram at @saltkettlecafe

Industry/Entity Type

Cafe / Restaurant

Contact Information for Business Card

Information equivalent to: Breakfast, Lunch, Dinner, Coffee, Takeaway / 918 Marlin Road Gullhaven SA 5291 / Menu & Opening Hours: www.saltkettlecafe.com.au / ph (08) 7194 2618

Requirements
Must have
• Information equivalent to: Breakfast, Lunch, Dinner, Coffee, Takeaway / 918 Marlin Road Gullhaven SA 5291 / Menu & Opening Hours: www.saltkettlecafe.com.au / ph (08) 7194 2618
Nice to have
• Potentially some of our trademark colours (Cafe can be searched via Google)
Should not have
• Must NOT have image of the building. May have the logo provided on one side but not necessarily, depending on how you wish to design the card

```html
<!DOCTYPE html>
<html lang="en">
<head>
<meta charset="utf-8">
<title>Salt Kettle Cafe – Business Card</title>
<link rel="stylesheet" href="https://fonts.googleapis.com/css2?family=Mulish:wght@400;600;700;800&display=swap">
<style>
  :root {
    --bg: #2b2b2d;
    --card: #ffffff;
    --card-shade: #eeeeee;
    --stitch: #c9c9c9;
    --navy: #1d4e8f;
    --rust: #b8591e;
    --ink: #3d3d3d;
  }
  * { box-sizing: border-box; margin: 0; padding: 0; }
  html, body { width: 1200px; height: 900px; overflow: hidden; }
  body {
    background: var(--bg);
    font-family: "Mulish", sans-serif;
    display: flex; flex-direction: column; align-items: center; justify-content: center;
    gap: 40px;
  }
  .card {
    position: relative;
    width: 620px; height: 354px;
    background: linear-gradient(135deg, var(--card) 55%, var(--card-shade));
    box-shadow: 0 10px 28px rgba(0,0,0,.45);
  }
  .card::before {
    content: ""; position: absolute; inset: 12px;
    border: 2px dashed var(--stitch);
    pointer-events: none;
  }
  .brand-name {
    color: var(--navy); font-weight: 800; text-transform: uppercase;
    letter-spacing: 1px; line-height: 1; text-align: center;
  }

  /* Front */
  .card-front { display: flex; flex-direction: column; align-items: center; }
  .card-front .brand-name { margin-top: 110px; font-size: 52px; }
  .card-front .rule { width: 470px; height: 0; border-top: 1.5px solid var(--navy); margin-top: 58px; }
  .card-front .web {
    margin-top: 16px; color: var(--rust); font-weight: 700; font-size: 15px;
    letter-spacing: 9px;
  }

  /* Back */
  .card-back { display: flex; flex-direction: column; align-items: center; padding-top: 34px; }
  .services { display: flex; align-items: flex-end; gap: 10px; }
  .service { display: flex; flex-direction: column; align-items: center; gap: 6px; }
  .service svg { width: 34px; height: 30px; stroke: var(--navy); fill: none; stroke-width: 1.6; stroke-linecap: round; stroke-linejoin: round; }
  .service span, .sep { color: var(--rust); font-weight: 700; font-size: 17px; letter-spacing: .5px; }
  .sep { padding-bottom: 1px; }
  .address { margin-top: 8px; color: var(--ink); font-weight: 700; font-size: 17px; }
  .card-back .brand-name { margin-top: 34px; font-size: 48px; }
  .menu-line { margin-top: 32px; color: var(--rust); font-weight: 800; font-size: 19px; }
  .contact { margin-top: 8px; display: flex; align-items: center; gap: 8px; color: var(--navy); font-weight: 700; font-size: 16px; }
  .contact svg { width: 16px; height: 16px; }
  .contact .bar { color: var(--ink); font-weight: 400; }
</style>
</head>
<body>

<section class="card card-front" aria-label="Business card front">
  <div class="brand-name">Salt Kettle<br>Cafe</div>
  <div class="rule"></div>
  <div class="web">www.saltkettlecafe.com.au</div>
</section>

<section class="card card-back" aria-label="Business card back">
  <div class="services">
    <div class="service">
      <svg viewBox="0 0 34 30"><circle cx="17" cy="15" r="13"/><circle cx="17" cy="15" r="9"/><circle cx="19" cy="17" r="3"/></svg>
      <span>BREAKFAST</span>
    </div>
    <span class="sep">|</span>
    <div class="service">
      <svg viewBox="0 0 34 30"><circle cx="17" cy="15" r="9"/><path d="M5 4v8M3 4v5a2 2 0 0 0 4 0V4M5 12v16M29 4c-3 2-3 8 0 10v14"/></svg>
      <span>LUNCH</span>
    </div>
    <span class="sep">|</span>
    <div class="service">
      <svg viewBox="0 0 34 30"><path d="M4 24h26M7 24a10 10 0 0 1 20 0M17 12v-2M13 7c1-2-1-3 0-5M21 7c1-2-1-3 0-5"/></svg>
      <span>DINNER</span>
    </div>
    <span class="sep">|</span>
    <div class="service">
      <svg viewBox="0 0 34 30"><path d="M8 12h16v6a6 6 0 0 1-6 6h-4a6 6 0 0 1-6-6zM24 14h2a3 3 0 0 1 0 6h-2M4 27h26M14 9c1-2-1-3 0-6M18 9c1-2-1-3 0-6"/></svg>
      <span>COFFEE</span>
    </div>
    <span class="sep">|</span>
    <div class="service">
      <svg viewBox="0 0 34 30"><path d="M13 4h14v22H13zM13 9h14M3 14h7M5 18h5M7 22h3"/></svg>
      <span>TAKEAWAY</span>
    </div>
  </div>
  <div class="address">918 Marlin Road Gullhaven SA 5291</div>
  <div class="brand-name">Salt Kettle Cafe</div>
  <div class="menu-line">Menu &amp; Opening Hours</div>
  <div class="contact">
    <svg viewBox="0 0 16 16" fill="#b8591e"><path d="M3 2h3l1 4-2 1a8 8 0 0 0 4 4l1-2 4 1v3a1 1 0 0 1-1 1A12 12 0 0 1 2 3a1 1 0 0 1 1-1z"/></svg>
    <span>(08) 7194 2618</span>
    <span class="bar">|</span>
    <svg viewBox="0 0 16 16" fill="none" stroke="#b8591e" stroke-width="1.5"><circle cx="8" cy="8" r="6.5"/><path d="M1.5 8h13M8 1.5c-3 3.5-3 9.5 0 13M8 1.5c3 3.5 3 9.5 0 13"/></svg>
    <span>www.saltkettlecafe.com.au</span>
  </div>
</section>

</body>
</html>
```